Corvale Holdings Business Cards

Hello. I need business cards designed with our new logo. I'd like to see at least 3 different designs. At least one with a dark background, and at least one with a white background. Maybe one with gray or blue for the background. Play with gradient colors and maybe even insert a pic of a skyline in the background of one or more of them. Use your judgement. We will need 2 cards printed. They need to accommodate the employee name, title, company address, phone, email, and website. Thanks.

Target Market(s)

Wealthy mature investors.

Contact Information for Business Card

Single-sided, professional, clean design that incorporates our logo.

Font styles to use
Sans Serif

Requirements
Must have
• Our new logo needs to be featured on it. (See attached.)
• Employee Name (In all CAPS)
• Title
• Street Address, City, ST Zip Code
• Cell Phone #, Email Address, Website Address
Nice to have
• Design that blends well with our new logo and its colors, or a city scape or other graphic design that looks like an apartment complex in the background. Blues and grays are nice, but use your judgement.
Should not have
• Modern or oriental looking designs or bright colors.

```html
<!DOCTYPE html>
<html lang="en">
<head>
<meta charset="utf-8">
<title>Corvale Holdings Business Card</title>
<link rel="stylesheet" href="https://fonts.googleapis.com/css2?family=Arimo:wght@400;700&family=Montserrat:wght@500&display=swap">
<style>
  :root {
    --night-deep: #0b0f16;
    --night-mid: #1a222e;
    --glow-warm: #3a3226;
    --brand-blue: #1f9be6;
    --text-white: #ffffff;
    --rule-white: #ffffff;
  }
  * { margin: 0; padding: 0; box-sizing: border-box; }
  html, body {
    width: 1200px; height: 601px; overflow: hidden;
    background: var(--night-deep);
  }
  .card {
    position: relative; width: 1200px; height: 601px; overflow: hidden;
    font-family: "Arimo", Arial, sans-serif; color: var(--text-white);
  }
  .skyline {
    position: absolute; inset: 0;
    background:
      radial-gradient(ellipse 70% 40% at 50% 70%, rgba(90,70,45,0.45), transparent 70%),
      linear-gradient(180deg, var(--night-deep) 0%, var(--night-mid) 35%, #232a33 55%, var(--glow-warm) 80%, #1a1a1c 100%);
  }
  .brand { position: absolute; left: 20px; top: 24px; display: flex; align-items: flex-start; gap: 22px; }
  .brand-square { width: 56px; height: 56px; background: var(--brand-blue); margin-top: 18px; }
  .brand-name {
    font-family: "Montserrat", Arial, sans-serif; font-weight: 500; color: var(--brand-blue);
    line-height: 1; letter-spacing: 1px;
  }
  .brand-name .line-main { display: block; font-size: 58px; margin-top: 18px; }
  .brand-name .line-sub { display: block; font-size: 34px; margin-top: 6px; }
  .rule { position: absolute; background: var(--rule-white); }
  .rule-h1 { left: 165px; top: 337px; width: 877px; height: 3px; }
  .rule-h2 { left: 165px; top: 438px; width: 877px; height: 3px; }
  .rule-v { left: 689px; top: 256px; width: 3px; height: 229px; }
  .person { position: absolute; right: 520px; top: 250px; text-align: right; }
  .person-name { font-size: 52px; font-weight: 400; line-height: 1; letter-spacing: 1px; }
  .person-name .surname { color: var(--brand-blue); }
  .person-title { font-size: 17px; font-weight: 700; margin-top: 12px; }
  .online { position: absolute; right: 520px; top: 352px; text-align: right; font-weight: 700; }
  .email { font-size: 28px; line-height: 1; }
  .website { font-size: 22px; margin-top: 17px; line-height: 1; }
  .phone { position: absolute; left: 699px; top: 290px; font-size: 29px; font-weight: 700; line-height: 1; }
  .address { position: absolute; left: 697px; top: 354px; font-size: 24px; font-weight: 700; line-height: 40px; }
</style>
</head>
<body>
  <div class="card">
    <div class="skyline" role="img" aria-label="Night-time city skyline with lit high-rise towers"></div>

    <div class="brand">
      <div class="brand-square"></div>
      <div class="brand-name">
        <span class="line-main">CORVALE</span>
        <span class="line-sub">HOLDINGS, LLC</span>
      </div>
    </div>

    <div class="rule rule-h1"></div>
    <div class="rule rule-h2"></div>
    <div class="rule rule-v"></div>

    <div class="person">
      <p class="person-name">EVAN <span class="surname">CORWELL</span></p>
      <p class="person-title">Principal (Manager) RL Heritage Partners, LLC</p>
    </div>

    <div class="online">
      <p class="email">contact@corvalemail.com</p>
      <p class="website">www.corvaleresidential.com</p>
    </div>

    <p class="phone">(555) 014-2870</p>
    <p class="address">418 Linden Ave Brook,<br>Millbrae, 70000, Texas</p>
  </div>
</body>
</html>
```